New letter head for Air Conditioning business

We need a new professional letter head design to suit our new re-branded air conditioning business. Our new logo is attached

```html
<!DOCTYPE html>
<html lang="en">
<head>
<meta charset="utf-8">
<title>Norvane Letterhead</title>
<link href="https://fonts.googleapis.com/css2?family=Open+Sans:wght@400;600&family=Lato:wght@400&display=swap" rel="stylesheet">
<style>
  :root {
    --backdrop: #e6e7e9;
    --paper: #ffffff;
    --accent-red: #ee6a5c;
    --accent-green: #67c38b;
    --ink: #444444;
    --ink-dark: #333333;
    --signature-tone: #e9eaec;
  }
  * { box-sizing: border-box; margin: 0; padding: 0; }
  html, body {
    width: 1040px; height: 1200px; overflow: hidden;
    background: var(--backdrop);
  }
  .letterhead {
    position: absolute; left: 53px; top: 0;
    width: 934px; height: 1200px;
    background: var(--paper);
    font-family: "Open Sans", Arial, sans-serif;
    color: var(--ink);
  }
  .top-band {
    position: absolute; left: 0; top: 0; width: 100%; height: 17px;
    background: var(--accent-red);
  }
  .brand {
    position: absolute; top: 50px; left: 0; width: 100%;
    display: flex; justify-content: center; align-items: center; gap: 14px;
  }
  .brand-dot {
    width: 44px; height: 44px; border-radius: 50%;
    background: var(--accent-green);
  }
  .brand-name {
    font-size: 42px; font-weight: 600; letter-spacing: 6px;
    color: var(--ink-dark);
  }
  .letter-body {
    position: absolute; left: 88px; right: 91px;
    font-size: 15px;
  }
  .issue-date { top: 218px; }
  .recipient { top: 254px; line-height: 18px; }
  .salutation { top: 358px; }
  .paragraph { line-height: 27px; text-align: justify; }
  .paragraph-one { top: 411px; }
  .paragraph-two { top: 573px; }
  .paragraph-three { top: 680px; }
  .closing { top: 816px; }
  .signature {
    position: absolute; left: 88px; top: 848px;
    width: 216px; height: 30px; border-radius: 4px;
    background: var(--signature-tone);
  }
  .signer-name {
    position: absolute; left: 88px; top: 892px;
    font-size: 19px; font-weight: 600; color: var(--ink-dark);
  }
  .signer-title {
    position: absolute; left: 88px; top: 922px; font-size: 15px;
  }
  .footer-band {
    position: absolute; left: 0; bottom: 0; width: 100%; height: 96px;
    background: var(--accent-green);
    font-family: "Lato", Arial, sans-serif;
    color: #ffffff; font-size: 17.5px;
    display: flex; flex-direction: column; align-items: center; justify-content: center; gap: 12px;
  }
  .footer-line { display: flex; align-items: center; gap: 10px; }
  .contact-item { display: flex; align-items: center; gap: 4px; }
  .contact-icon { width: 21px; height: 21px; flex: none; }
</style>
</head>
<body>
  <main class="letterhead">
    <div class="top-band"></div>

    <header class="brand">
      <span class="brand-dot"></span>
      <span class="brand-name">NORVANE</span>
    </header>

    <p class="letter-body issue-date">Issuing Date: May 5, 2018</p>
    <p class="letter-body recipient">Name Of Employee Mr. XYZABC<br>Address of Employee<br>Address Line 2 etc..</p>
    <p class="letter-body salutation">Dear Mr.XYZABC</p>

    <p class="letter-body paragraph paragraph-one">Lorem Ipsum has been the industry's standard dummy text ever since the 1500s, when an unknown printer took a galley of type and scrambled it to make a type specimen book. It has survived not only five centuries, but also the leap into electronic typesetting, remaining essentially unchanged. It was popularised in the 1960s with the release of Typeline sheets containing Lorem Ipsum passages, and more recently with desktop publishing software like Folio Press including versions of Lorem Ipsum.</p>
    <p class="letter-body paragraph paragraph-two">Lorem Ipsum is simply dummy text of the printing and typesetting industry. Lorem Ipsum has been the industry's standard dummy text ever since the 1500s, when an unknown printer took a galley of type and scrambled it to make a type specimen book.</p>
    <p class="letter-body paragraph paragraph-three">It has survived not only five centuries, but also the leap into electronic typesetting, remaining essentially unchanged. It was popularised in the 1960s with the release of Typeline sheets containing Lorem IpsumIpsum passages.</p>

    <p class="letter-body closing">Yours Sincerely</p>
    <div class="signature" role="img" aria-label="Handwritten signature of Marcus Hale"></div>
    <p class="signer-name">Marcus Hale</p>
    <p class="signer-title">Managing Director</p>

    <footer class="footer-band">
      <div class="footer-line">
        <span class="contact-item">
          <svg class="contact-icon" viewBox="0 0 20 20" aria-hidden="true"><circle cx="10" cy="10" r="10" fill="#fff"/><path d="M10 4.5a3.6 3.6 0 0 0-3.6 3.6c0 2.7 3.6 7 3.6 7s3.6-4.3 3.6-7A3.6 3.6 0 0 0 10 4.5z" fill="#67c38b"/><circle cx="10" cy="8.1" r="1.4" fill="#fff"/></svg>
          87, Harbour Row Eastfield Country, 30918
        </span>
      </div>
      <div class="footer-line">
        <span class="contact-item">
          <svg class="contact-icon" viewBox="0 0 20 20" aria-hidden="true"><circle cx="10" cy="10" r="10" fill="#fff"/><path d="M7 5l2 2.6-1.1 1.3c.7 1.4 1.8 2.5 3.2 3.2l1.3-1.1L15 13l-1.2 1.8C9.6 14.6 5.4 10.4 5.2 6.2z" fill="#67c38b"/></svg>
          051-372 604 118
        </span>
        <span class="contact-item">
          <svg class="contact-icon" viewBox="0 0 20 20" aria-hidden="true"><circle cx="10" cy="10" r="10" fill="#fff"/><rect x="5" y="6.5" width="10" height="7" rx="1" fill="#67c38b"/><path d="M5.5 7l4.5 3.5L14.5 7" stroke="#fff" stroke-width="1" fill="none"/></svg>
          hello@norvane.co
        </span>
        <span class="contact-item">
          <svg class="contact-icon" viewBox="0 0 20 20" aria-hidden="true"><circle cx="10" cy="10" r="10" fill="#fff"/><circle cx="10" cy="10" r="5.5" fill="#67c38b"/><path d="M4.5 10h11M10 4.5c-2.2 2.8-2.2 8.2 0 11M10 4.5c2.2 2.8 2.2 8.2 0 11" stroke="#fff" stroke-width="0.9" fill="none"/></svg>
          www.norvane-air.com
        </span>
      </div>
    </footer>
  </main>
</body>
</html>
```